Pitch deck power point presentation template

I need a power point template for a pitch deck for a startup biotechnology company using the logo we purchased from pixelharbor. It should have a cover page and content pages that we can adapt to fit multiple presentations. It should have a page for the team and advisors, and pages for graphs and charts, also pages that have space to add pictures to give background information, and then some with general pages with some blank space. I want it to catch the eye but also be very professional looking.
Updates

The original deadline was only one day from posting for some reason, I extended to 5 days to allow more time.

Target Market(s)

Investors

Industry/Entity Type

Biotechnology

Font styles to use
Serif
Sans Serif

Colors
0054AA
0677BA
7BADD7
CADEEF
E8F1F8

Requirements
Must have
• The logo and the blue color from the logo as the primary color used
Nice to have
• other layouts that we can select from

```html
<!DOCTYPE html>
<html lang="en">
<head>
<meta charset="utf-8">
<title>Corvane Therapeutics — Pitch Deck Template</title>
<link href="https://fonts.googleapis.com/css2?family=Exo+2:wght@500;600;700&family=Poppins:wght@400;500;600&display=swap" rel="stylesheet">
<style>
:root{
  --board:#7d7e80;
  --blue-deep:#0054AA;
  --blue:#0677BA;
  --blue-bright:#1f8ad0;
  --blue-soft:#7BADD7;
  --blue-pale:#CADEEF;
  --blue-mist:#E8F1F8;
  --teal:#2a9a7e;
  --teal-title:#27948a;
  --ink:#222528;
  --slate:#3d4045;
  --grey-text:#555a60;
  --white:#ffffff;
}
*{box-sizing:border-box;margin:0;padding:0}
html,body{width:1200px;height:4231px;overflow:hidden}
body{background:var(--board);position:relative;font-family:"Poppins",sans-serif;color:var(--ink)}
.slide{position:absolute;left:59px;width:1082px;height:607px;overflow:hidden;background:var(--white)}
.abs{position:absolute}
.heading{font-family:"Exo 2",sans-serif;font-weight:600}
.brand-mini{position:absolute;right:62px;top:44px;display:flex;align-items:center;gap:6px;font-family:"Exo 2",sans-serif;font-weight:600;font-size:15px;color:var(--teal)}
.brand-mini .dot{width:12px;height:12px;border-radius:50%;background:var(--teal)}
.social{display:flex;gap:8px}
.social span{display:block;width:30px;height:30px;border-radius:50%;border:1.5px solid currentColor}

/* cover */
.cover{top:84px;background:linear-gradient(110deg,#e6eef4 0%,#f1f5f8 40%,#dde9f0 70%,#cfe0ea 100%)}
.cover-photo{position:absolute;inset:0;background:radial-gradient(ellipse at 75% 40%,rgba(160,200,215,.55),transparent 60%),radial-gradient(ellipse at 20% 85%,rgba(190,210,220,.6),transparent 55%)}
.cover-brand{position:absolute;left:67px;top:64px;display:flex;align-items:center;gap:10px;font-family:"Exo 2",sans-serif;font-weight:600;font-size:32px;color:var(--blue)}
.cover-brand .dot{width:22px;height:22px;border-radius:50%;background:var(--blue)}
.cover-title{position:absolute;left:58px;top:190px;font-family:"Exo 2",sans-serif;font-weight:600;font-size:140px;line-height:1;color:var(--blue-bright)}
.cover-sub{position:absolute;left:64px;top:355px;font-family:"Exo 2",sans-serif;font-weight:600;font-size:62px;line-height:1;color:var(--teal)}
.cover .social{position:absolute;left:64px;top:530px;color:var(--blue)}
.cover-orb{position:absolute;left:560px;top:120px;width:480px;height:420px;border-radius:50%;background:radial-gradient(circle,rgba(120,170,190,.35),rgba(120,170,190,0) 70%)}

/* about */
.about{top:762px}
.about-panel{position:absolute;left:0;top:0;width:541px;height:607px;background:var(--teal)}
.slide-title{position:absolute;left:64px;top:40px;font-family:"Exo 2",sans-serif;font-weight:600;font-size:32px;line-height:1.2}
.star{position:absolute;left:-4px;top:37px;width:60px;height:58px}
.about .slide-title{color:var(--white)}
.about-copy{position:absolute;left:64px;top:148px;width:386px;font-size:12.4px;line-height:24.6px;color:#e9f5f1;text-align:justify}
.about-photo{position:absolute;left:541px;top:0;width:541px;height:607px;background:radial-gradient(circle at 50% 48%,#1f5fd0 0%,#3a7fe0 18%,#8fb5ea 42%,#c9b8e0 70%,#e7d0e6 100%)}
.about .brand-mini{color:var(--white)}
.about .brand-mini .dot{background:var(--white)}

/* services */
.services{top:1448px;background:linear-gradient(120deg,#f2f4f6 0%,#ffffff 55%,#f5f7f8 100%)}
.services .slide-title{color:var(--teal-title)}
.service{position:absolute;width:184px}
.service h3{font-family:"Poppins",sans-serif;font-weight:500;font-size:16px;color:var(--ink);margin-bottom:10px}
.service p{font-size:8.6px;line-height:14px;color:var(--grey-text);text-align:justify}
.service.right{text-align:right}
.service.right p{text-align:justify;text-align-last:right}
.service-icon{width:34px;height:34px;margin-bottom:10px;display:block}
.service.right .service-icon{margin-left:auto}

/* feature */
.feature{top:2139px}
.feature-photo{position:absolute;left:0;top:0;width:760px;height:607px;background:linear-gradient(90deg,#1d4f9a 0%,#2f74c4 35%,#8fb7e0 65%,rgba(255,255,255,0) 100%)}
.feature h2{position:absolute;left:561px;top:122px;font-family:"Exo 2",sans-serif;font-weight:600;font-size:32px;color:var(--ink)}
.checklist{position:absolute;left:561px;top:194px;width:470px;list-style:none}
.checklist li{position:relative;padding-left:30px;font-size:15.5px;line-height:25px;color:#30343a;margin-bottom:17px}
.checklist svg{position:absolute;left:0;top:4px;width:17px;height:17px}

/* team */
.team{top:2842px;background:linear-gradient(135deg,#2a8ad6 0%,#1b78c6 50%,#1669b4 100%)}
.team .slide-title{color:var(--white)}
.team .brand-mini{color:var(--white)}
.team .brand-mini .dot{background:var(--white)}
.member{position:absolute;top:168px;width:222px;text-align:center}
.member-photo{margin:0 auto;width:213px;height:193px;background:linear-gradient(180deg,#d7e2ea 0%,#b9cbd8 100%)}
.member-name{margin-top:3px;height:41px;background:var(--white);font-family:"Exo 2",sans-serif;font-weight:500;font-size:17px;line-height:41px;color:var(--blue-bright)}
.member-bio{margin-top:26px;font-size:9.8px;line-height:16px;color:#e4f0fa;padding:0 12px}
.member .social{justify-content:center;margin-top:16px;color:var(--white)}

/* closing */
.closing{top:3538px;background:linear-gradient(120deg,#f3f6f8 0%,#ffffff 50%,#f7fafb 100%)}
.closing h2{position:absolute;left:61px;top:162px;font-family:"Exo 2",sans-serif;font-weight:600;font-size:40px;color:var(--blue-bright)}
.presenter{position:absolute;left:61px;top:276px;font-weight:600;font-size:16px;color:var(--ink);letter-spacing:.3px}
.contact{position:absolute;left:61px;list-style:none;width:320px}
.contact li{position:absolute;left:0;display:flex;gap:12px;align-items:flex-start;font-size:11.5px;line-height:16px;color:#3a3f45;width:320px}
.contact svg{flex:none;width:17px;height:17px;fill:var(--blue-bright)}
.closing-brand{position:absolute;left:560px;top:262px;display:flex;align-items:center;gap:18px;font-family:"Exo 2",sans-serif;font-weight:600;font-size:58px;line-height:1;color:var(--blue-bright)}
.closing-brand .dot{width:36px;height:36px;border-radius:50%;background:var(--blue-bright)}
.closing-arc{position:absolute;left:520px;top:60px;width:600px;height:520px;border-radius:50%;border:26px solid rgba(123,173,215,.12)}
</style>
</head>
<body>

<!-- Cover -->
<section class="slide cover">
  <div class="cover-photo" role="img" aria-label="Soft laboratory backdrop with glassware and molecule models in pale blue tones"></div>
  <div class="cover-orb"></div>
  <div class="cover-brand"><span class="dot"></span>Corvane Therapeutics</div>
  <div class="cover-title">Corvane</div>
  <div class="cover-sub">Therapeutics</div>
  <div class="social"><span></span><span></span><span></span><span></span></div>
</section>

<!-- About -->
<section class="slide about">
  <div class="about-panel">
    <svg class="star" viewBox="0 0 60 58"><polygon fill="#fff" points="30,0 37,21 60,21 41,35 48,58 30,44 12,58 19,35 0,21 23,21"/></svg>
    <h2 class="slide-title">About Corvane Therapeutics</h2>
    <p class="about-copy">Lorem ipsum dolor sit amet, consectetur adipiscing elit, sed do eiusmod tempor incididunt ut labore et dolore magna aliqua. Ut enim ad minim veniam, quis nostrud exercitation ullamco laboris nisi ut aliquip ex ea commodo consequat. Duis aute irure dolor in reprehenderit in voluptate velit esse cillum dolore eu fugiat nulla pariatur. Excepteur sint occaecat cupidatat non proident, sunt in culpa qui officia deserunt mollit anim id est laborum. Sed ut perspiciatis unde omnis iste natus error sit voluptatem accusantium doloremque laudantium, totam rem aperiam, eaque ipsa quae ab illo inventore veritatis et quasi architecto beatae vitae dicta sunt explicabo.</p>
  </div>
  <div class="about-photo" role="img" aria-label="Close-up of a glowing blue cell cluster in a translucent droplet"></div>
  <div class="brand-mini"><span class="dot"></span>Corvane</div>
</section>

<!-- Services -->
<section class="slide services">
  <svg class="star" viewBox="0 0 60 58"><polygon fill="#1f8ad0" points="30,0 37,21 60,21 41,35 48,58 30,44 12,58 19,35 0,21 23,21"/></svg>
  <h2 class="slide-title">Our Services</h2>
  <div class="brand-mini"><span class="dot"></span>Corvane</div>

  <svg class="abs" style="left:0;top:0" width="1082" height="607" viewBox="0 0 1082 607">
    <line x1="212" y1="317" x2="868" y2="317" stroke="#555" stroke-width="2" stroke-dasharray="2 5"/>
    <line x1="540" y1="150" x2="540" y2="485" stroke="#555" stroke-width="2" stroke-dasharray="2 5"/>
    <g transform="translate(540 317)">
      <polygon fill="#3d4045" points="-4,-4 -4,-125 -40,-90 -115,-115 -90,-40 -125,-4"/>
      <polygon fill="#2a9a7e" transform="scale(-1 1)" points="-4,-4 -4,-125 -40,-90 -115,-115 -90,-40 -125,-4"/>
      <polygon fill="#1f8ad0" transform="scale(1 -1)" points="-4,-4 -4,-125 -40,-90 -115,-115 -90,-40 -125,-4"/>
      <polygon fill="#3d4045" transform="scale(-1 -1)" points="-4,-4 -4,-125 -40,-90 -115,-115 -90,-40 -125,-4"/>
      <circle r="40" fill="#fff"/>
      <g font-family="Exo 2, sans-serif" font-weight="700" font-size="26" fill="#fff" text-anchor="middle">
        <text x="-55" y="-44">01</text>
        <text x="55" y="-44">03</text>
        <text x="-55" y="72">02</text>
        <text x="55" y="72">04</text>
      </g>
    </g>
  </svg>

  <div class="service" style="left:212px;top:136px">
    <svg class="service-icon" viewBox="0 0 34 34" fill="none" stroke="#3d4045" stroke-width="1.6"><rect x="4" y="6" width="22" height="20" rx="2"/><line x1="8" y1="12" x2="22" y2="12"/><line x1="8" y1="17" x2="18" y2="17"/><circle cx="26" cy="24" r="5"/></svg>
    <h3>Implementation</h3>
    <p>Lorem ipsum dolor sit amet, consectetur adipiscing elit, sed do eiusmod tempor incididunt ut labore et dolore magnaaliqua. Ut enim ad minim veniam, quis nostrud exercitation ullamco laboris nisi ut commodo consequat.</p>
  </div>
  <div class="service right" style="left:685px;top:136px">
    <svg class="service-icon" viewBox="0 0 34 34" fill="none" stroke="#2a9a7e" stroke-width="1.6"><path d="M12 4h8M14 4v9L6 28h20L18 13V4"/><circle cx="26" cy="8" r="3"/></svg>
    <h3>Biotechnology</h3>
    <p>Lorem ipsum dolor sit amet, consectetur adipiscing elit, sed do eiusmod tempor incididunt ut labore et dolore magnaaliqua. Ut enim ad minim veniam, quis nostrud exercitation ullamco laboris nisi ut commodo consequat.</p>
  </div>
  <div class="service" style="left:212px;top:350px">
    <svg class="service-icon" viewBox="0 0 34 34" fill="none" stroke="#1f8ad0" stroke-width="1.6"><circle cx="17" cy="11" r="6"/><path d="M6 30c0-7 5-11 11-11s11 4 11 11"/></svg>
    <h3>Support Services</h3>
    <p>Lorem ipsum dolor sit amet, consectetur adipiscing elit, sed do eiusmod tempor incididunt ut labore et dolore magnaaliqua. Ut enim ad minim veniam, quis nostrud exercitation ullamco laboris nisi ut aliquip ex ea commodo consequat.</p>
  </div>
  <div class="service right" style="left:685px;top:350px">
    <svg class="service-icon" viewBox="0 0 34 34" fill="none" stroke="#3d4045" stroke-width="1.6"><rect x="6" y="4" width="20" height="26" rx="2"/><line x1="10" y1="16" x2="22" y2="16"/><line x1="10" y1="21" x2="20" y2="21"/><circle cx="26" cy="27" r="4"/></svg>
    <h3>Health Check</h3>
    <p>Lorem ipsum dolor sit amet, consectetur adipiscing elit, sed do eiusmod tempor incididunt ut labore et dolore magnaaliqua. Ut enim ad minim veniam, quis nostrud exercitation ullamco laboris nisi ut aliquip ex ea commodo consequat.</p>
  </div>
</section>

<!-- Feature -->
<section class="slide feature">
  <div class="feature-photo" role="img" aria-label="Laboratory scientist in safety glasses holding a sample tube over a notebook"></div>
  <div class="brand-mini"><span class="dot"></span>Corvane</div>
  <h2>Lorem ipsum dolor sit</h2>
  <ul class="checklist">
    <li><svg viewBox="0 0 17 17"><circle cx="8.5" cy="8.5" r="8.5" fill="#2a9a7e"/><path d="M4.5 8.7l2.6 2.6 5.3-5.3" stroke="#fff" stroke-width="2" fill="none"/></svg>Lorem ipsum dolor sit amet, consectetur adipiscing elit</li>
    <li><svg viewBox="0 0 17 17"><circle cx="8.5" cy="8.5" r="8.5" fill="#2a9a7e"/><path d="M4.5 8.7l2.6 2.6 5.3-5.3" stroke="#fff" stroke-width="2" fill="none"/></svg>Duis aute irure dolor in reprehenderit in voluptate velit esse cillum</li>
    <li><svg viewBox="0 0 17 17"><circle cx="8.5" cy="8.5" r="8.5" fill="#2a9a7e"/><path d="M4.5 8.7l2.6 2.6 5.3-5.3" stroke="#fff" stroke-width="2" fill="none"/></svg>Excepteur sint occaecat cupidatat non proident, sunt in culpa qui officia deserunt</li>
    <li><svg viewBox="0 0 17 17"><circle cx="8.5" cy="8.5" r="8.5" fill="#2a9a7e"/><path d="M4.5 8.7l2.6 2.6 5.3-5.3" stroke="#fff" stroke-width="2" fill="none"/></svg>Sed ut perspiciatis unde omnis iste natus error sit volup accusantium doloremque</li>
    <li><svg viewBox="0 0 17 17"><circle cx="8.5" cy="8.5" r="8.5" fill="#2a9a7e"/><path d="M4.5 8.7l2.6 2.6 5.3-5.3" stroke="#fff" stroke-width="2" fill="none"/></svg>Nemo enim ipsam voluptatem quia voluptas sit asperna aut odit aut fugit, sed quia consequuntur</li>
  </ul>
</section>

<!-- Team -->
<section class="slide team">
  <svg class="star" viewBox="0 0 60 58"><polygon fill="#fff" points="30,0 37,21 60,21 41,35 48,58 30,44 12,58 19,35 0,21 23,21"/></svg>
  <h2 class="slide-title">Our Team</h2>
  <div class="brand-mini"><span class="dot"></span>Corvane</div>

  <div class="member" style="left:60px">
    <div class="member-photo" role="img" aria-label="Portrait of a team member in a white lab coat"></div>
    <div class="member-name">John Smith</div>
    <p class="member-bio">Lorem ipsum dolor sit amet, consectetur adipiscing elitsed do eiusmod tempor incididunt</p>
    <div class="social"><span></span><span></span><span></span><span></span></div>
  </div>
  <div class="member" style="left:307px">
    <div class="member-photo" role="img" aria-label="Portrait of a team member in a white lab coat"></div>
    <div class="member-name">John Smith</div>
    <p class="member-bio">Lorem ipsum dolor sit amet, consectetur adipiscing elitsed do eiusmod tempor incididunt</p>
    <div class="social"><span></span><span></span><span></span><span></span></div>
  </div>
  <div class="member" style="left:555px">
    <div class="member-photo" role="img" aria-label="Portrait of a team member in a white lab coat"></div>
    <div class="member-name">John Smith</div>
    <p class="member-bio">Lorem ipsum dolor sit amet, consectetur adipiscing elitsed do eiusmod tempor incididunt</p>
    <div class="social"><span></span><span></span><span></span><span></span></div>
  </div>
  <div class="member" style="left:802px">
    <div class="member-photo" role="img" aria-label="Portrait of a team member in a white lab coat"></div>
    <div class="member-name">John Smith</div>
    <p class="member-bio">Lorem ipsum dolor sit amet, consectetur adipiscing elitsed do eiusmod tempor incididunt</p>
    <div class="social"><span></span><span></span><span></span><span></span></div>
  </div>
</section>

<!-- Closing -->
<section class="slide closing">
  <div class="closing-arc"></div>
  <h2>Thank you</h2>
  <div class="presenter">PRESENTER NAME</div>
  <ul class="contact">
    <li style="top:322px"><svg viewBox="0 0 24 24"><path d="M6.6 10.8a15 15 0 006.6 6.6l2.2-2.2a1 1 0 011-.25 11.4 11.4 0 003.6.57 1 1 0 011 1V20a1 1 0 01-1 1A17 17 0 013 4a1 1 0 011-1h3.5a1 1 0 011 1c0 1.25.2 2.45.57 3.6a1 1 0 01-.25 1z"/></svg>(555) 014 2290</li>
    <li style="top:360px"><svg viewBox="0 0 24 24"><path d="M12 2a10 10 0 100 20 10 10 0 000-20zm6.9 6h-3a15.7 15.7 0 00-1.4-3.6A8 8 0 0118.9 8zM12 4c.8 1.2 1.5 2.5 1.9 4h-3.8c.4-1.5 1.1-2.8 1.9-4zM4.3 14a8 8 0 010-4h3.4a16 16 0 000 4zm.8 2h3a15.7 15.7 0 001.4 3.6A8 8 0 015.1 16zm3-8h-3a8 8 0 014.4-3.6A15.7 15.7 0 008.1 8zM12 20c-.8-1.2-1.5-2.5-1.9-4h3.8c-.4 1.5-1.1 2.8-1.9 4zm2.3-6H9.7a14.6 14.6 0 010-4h4.6a14.6 14.6 0 010 4zm.2 5.6a15.7 15.7 0 001.4-3.6h3a8 8 0 01-4.4 3.6zm1.8-5.6a16 16 0 000-4h3.4a8 8 0 010 4z"/></svg>www.corvanetherapeutics.com</li>
    <li style="top:396px"><svg viewBox="0 0 24 24"><path d="M2 5h20v14H2zm2 2v.5l8 5 8-5V7zm0 2.8V17h16V9.8l-8 5z"/></svg>info@corvanetherapeutics.com</li>
    <li style="top:430px"><svg viewBox="0 0 24 24"><path d="M12 2a7 7 0 00-7 7c0 5.2 7 13 7 13s7-7.8 7-13a7 7 0 00-7-7zm0 9.5A2.5 2.5 0 1112 6.5a2.5 2.5 0 010 5z"/></svg>123,Lorem ipsum dolor sit amet, consectetur adipiscing elit</li>
  </ul>
  <div class="closing-brand"><span class="dot"></span>Corvane Therapeutics</div>
</section>

</body>
</html>
```